Business Card Design

We need a business card design that can also be aplied for postcards. We are a small indie record company that also do consulting, and development of independat artitst . I already have the name and the basic idea of what i am looking for but i am open to any suggestion.
Info for the card
Name of the company : Velmora Records
NAME : Tomas Invaldi
PHONE : 208-5536142
EMAIL : hello@velmorarecords.example
WEB: www.velmorarecords.example
Target Market(s)
Male - Female independent musicians ages 18 to 45
Industry/Entity Type
Record Company
Contact Information for Business Card
Independant records company that also works in consulting for music business models for independent artists
Look and feel
Each slider illustrates characteristics of the customer's brand and the style your logo design should communicate.

```html
<!DOCTYPE html>
<html lang="en">
<head>
<meta charset="utf-8">
<title>Velmora Records — Business Card</title>
<link rel="stylesheet" href="https://fonts.googleapis.com/css2?family=PT+Sans+Narrow:wght@400;700&family=Quicksand:wght@500&display=swap">
<style>
  :root {
    --page: #ffffff;
    --card-edge: #d6d6d6;
    --card-outer: #f1f1f1;
    --card-inner: #ffffff;
    --orange: #e8720c;
    --ink: #111111;
    --art-grey: #bdbdbd;
    --art-dark: #2a2a2a;
  }
  * { margin: 0; padding: 0; box-sizing: border-box; }
  html, body {
    width: 1200px;
    height: 997px;
    overflow: hidden;
    background: var(--page);
  }
  .canvas {
    position: relative;
    width: 1200px;
    height: 997px;
  }
  .card {
    position: absolute;
    width: 604px;
    height: 338px;
    border: 2px solid var(--card-edge);
    background: radial-gradient(ellipse 70% 75% at 45% 45%, var(--card-inner) 0%, var(--card-inner) 35%, var(--card-outer) 100%);
    overflow: hidden;
  }
  .card--front { left: 106px; top: 144px; }
  .card--back  { left: 494px; top: 518px; }

  .artwork {
    position: absolute;
    border-radius: 50%;
  }
  .card--front .artwork {
    left: 70px; top: 56px;
    width: 204px; height: 210px;
    background: radial-gradient(circle at 52% 45%, var(--art-dark) 0%, var(--orange) 22%, var(--art-grey) 48%, rgba(200,200,200,0.35) 70%, rgba(255,255,255,0) 100%);
  }
  .card--back .artwork {
    left: 0; top: 10px;
    width: 240px; height: 290px;
    opacity: 0.22;
    background: radial-gradient(circle at 55% 45%, var(--art-dark) 0%, var(--orange) 22%, var(--art-grey) 48%, rgba(200,200,200,0.35) 70%, rgba(255,255,255,0) 100%);
  }

  .brand {
    position: absolute;
    right: 36px;
    top: 30px;
    text-align: right;
    font-family: "Quicksand", sans-serif;
    font-weight: 500;
    color: var(--orange);
    font-size: 40px;
    line-height: 1;
    letter-spacing: 0.5px;
  }
  .contact {
    position: absolute;
    right: 34px;
    top: 222px;
    text-align: right;
    font-family: "PT Sans Narrow", sans-serif;
  }
  .contact__name {
    font-weight: 700;
    font-size: 26px;
    color: var(--ink);
    line-height: 1;
    margin-bottom: 10px;
  }
  .contact__line {
    font-size: 18px;
    color: var(--orange);
    line-height: 28px;
  }
  .web {
    position: absolute;
    left: 0; right: 0;
    top: 161px;
    text-align: center;
    padding-left: 20px;
    font-family: "PT Sans Narrow", sans-serif;
    font-size: 19px;
    color: var(--orange);
  }
</style>
</head>
<body>
  <main class="canvas">
    <section class="card card--front" aria-label="Business card front">
      <div class="artwork" role="img" aria-label="Splash illustration of a turntable with orange and grey circles"></div>
      <div class="brand">Velmora Records</div>
      <div class="contact">
        <p class="contact__name">Tomas Invaldi</p>
        <p class="contact__line">Call: 208-5536142</p>
        <p class="contact__line">Email: hello@velmorarecords.example</p>
      </div>
    </section>

    <section class="card card--back" aria-label="Business card back">
      <div class="artwork" role="img" aria-label="Faded turntable splash illustration in the background"></div>
      <p class="web">www.velmorarecords.example</p>
    </section>
  </main>
</body>
</html>
```